Hospital Website Design - PSD only

We need a web design for a community hospital based in Uniontown, Pennsylvania.

We would like to see a first round of designs for the website HOMEPAGE. Once we have selected finalists for the look & feel, based on the submitted homepage designs, we will request an additional INTERNAL page design.

Both designs should follow the content requirements displayed on the attached wireframes. I will post the internal page wireframe after the homepage design finalists are selected.

The desired Look & Feel for the website is clean and modern.

3 sites we like are:
http://www.marvellcare.org/
http://www.qrtm.org/
http://www.dellwyn.org/

Attached are the Homepage wireframe, and the Brackfield Hospital Logo.

The winning design will communicate a bright, healthy, energetic, community-oriented feeling.

Please note that readability is very important for a hospital website. Font-sizes and line-heights should be carefully selected for comfortable reading.
Updates

Dear designers -- Please don't feel locked into the exact shades of blue / brown used in the logo. We find this color scheme quite ugly and are working on a logo update. The new color scheme will probably still involve some shades of blue and brown, but we aren't sure yet. Please use your best judgement to make a beautiful design, similar in style to the modern / simple aesthetic of http://www.marvellcare.org/ We will be working on feedback to designs today. Thank you.

Regarding Large Rotating Graphic area and Navigation: We prefer a full-width display, rather than boxed. The navigation should be visually prominent, easy to read text that one can scan easily across the top of the page. Again, please refer to http://www.marvellcare.org/ for our preferred design aesthetic. Some of the designs submitted have been somewhat dated in their styling. We'd like a polished, modern, crisp, bold, beautiful design.

Re: choice of image in large rotating graphic area -- Designers, please do not use stock photography of a group of doctors, or a nursing home scene, in your sample rotating graphic areas. Although this should not affect our perception of the design, it throws off everything in the page if we don't like the image. Please try to select a bold / attractive image that you would like to set the tone for your design.

Reason: Extending our deadline to receive more designs exploring other color options containing less brown, or browns with a more attractive vibe. We would also like to see designs that are not exact replicas of the wireframe. The wireframe is just to show the elements on the page. Please use your creativity to utilize these elements in an attractive layout that we will like. We would also prefer to see use of photography that shows a younger, more cheerful, hopeful feeling in the design... and where the photographs are consistent with your design approach. Thanks!

In general, feedback for everyone is, please look here: http://www.marvellcare.org/ that's the feeling / vibe we want. DO NOT let the old, ugly, outdated logo determine your design. We are having the logo redesigned. DO NOT take an ugly, outdated template, and adapt it for this website. We want to see something BEAUTIFUL!!! Please give us your best effort! People who come to this website are in health crisis, and they want to be uplifted!! Their good spirits are in your hands.

Reason: We are still reviewing submissions and working with designers to provide better feedback. Thanks for your patience.

Reason: our sincerest apologies for the failure to provide adequate feedback this week. We hit a snag with the various decision makers on this project and were not able to review the recent submissions. We will make every effort to have a decision by tomorrow. Thank you for your patience.

Target Market(s)

Adults based in suburban & rural community, aged 18-80.

Industry/Entity Type

Hospital

Requirements
Must have
• The design must include all of the content areas outlined on the attached wireframe.
The design must include the attached logo. (Note, we may update the logo during the design contest, but it will not be changed dramatically. It will just be modernized slightly.)
Nice to have
• Show hover states for things like Navigation, Links, or small images in gallery, so we can see how you imagine interactive states.

```html
<!DOCTYPE html>
<html lang="en">
<head>
<meta charset="utf-8">
<title>Brackfield Hospital</title>
<link href="https://fonts.googleapis.com/css2?family=Open+Sans:wght@400;600;700&display=swap" rel="stylesheet">
<style>
:root{
  --blue:#1a7de8;
  --blue-dark:#1268c9;
  --coral:#e26a5c;
  --coral-dark:#cf5a4c;
  --slate:#3b4e63;
  --slate-dark:#2f4053;
  --ink:#2e3a46;
  --muted:#8c97a3;
  --line:#e4e8ec;
  --white:#ffffff;
}
*{box-sizing:border-box;margin:0;padding:0}
html,body{width:752px;height:1200px;overflow:hidden}
body{font-family:"Open Sans",Arial,sans-serif;font-weight:400;color:var(--ink);background:var(--white);position:relative}
.abs{position:absolute}
a{color:inherit;text-decoration:none}
ul{list-style:none}

/* chevron inside circle */
.chev{position:relative;display:inline-block;border-radius:50%}
.chev::before{content:"";position:absolute;left:50%;top:50%;width:3px;height:3px;border-top:1px solid currentColor;border-right:1px solid currentColor;transform:translate(-65%,-50%) rotate(45deg)}
.chev.left::before{transform:translate(-35%,-50%) rotate(-135deg)}

/* top bar */
.topbar{left:0;top:0;width:752px;height:28px;background:linear-gradient(#4a5d72,#34465a);color:#e9eef3;font-size:6.5px}
.topbar .item{position:absolute;top:10px;display:flex;align-items:center;gap:4px}
.topbar .sep{position:absolute;top:0;width:1px;height:28px;background:rgba(255,255,255,.12)}
.topbar svg{display:block}

/* header */
.header{left:0;top:28px;width:752px;height:77px;background:var(--white)}
.logo{left:101px;top:33px;display:flex;align-items:center;gap:6px}
.logo .mark{width:9px;height:9px;background:var(--slate);border-radius:50%}
.logo .name{font-size:11px;font-weight:600;color:var(--slate);letter-spacing:.3px}
.social{left:604px;top:13px;display:flex;gap:7px}
.social i{display:block;width:7px;height:7px;border-radius:2px;background:var(--slate)}
.search{left:547px;top:32px;width:104px;height:17px;border:1px solid #d5dbe1;border-radius:3px;font-size:5.5px;color:#b3bcc5;padding:4px 7px;font-style:italic}
.search b{position:absolute;right:-1px;top:-1px;width:17px;height:17px;background:var(--slate);border-radius:0 3px 3px 0;display:flex;align-items:center;justify-content:center}

/* nav */
.nav{left:0;top:105px;width:752px;height:27px;background:linear-gradient(#2b8cf4,#167be6)}
.nav a{position:absolute;top:0;height:27px;line-height:27px;text-align:center;font-size:7.4px;font-weight:400;color:var(--white);border-left:1px solid rgba(0,0,0,.14)}
.nav a.active{color:#8fc2fb}

/* hero */
.hero{left:0;top:132px;width:752px;height:268px;overflow:hidden;
  background:
    linear-gradient(rgba(40,55,75,.08),rgba(40,55,75,.18)),
    radial-gradient(ellipse 90px 70px at 500px 60px,rgba(236,198,170,.9),rgba(236,198,170,0)),
    radial-gradient(ellipse 150px 120px at 215px 130px,rgba(232,186,150,.95),rgba(232,186,150,0)),
    radial-gradient(ellipse 110px 50px at 120px 90px,rgba(214,170,110,.8),rgba(214,170,110,0)),
    radial-gradient(ellipse 180px 70px at 200px 250px,rgba(245,246,248,.95),rgba(245,246,248,0)),
    radial-gradient(ellipse 60px 60px at 40px 230px,rgba(236,230,222,.9),rgba(236,230,222,0)),
    radial-gradient(ellipse 16px 60px at 610px 140px,rgba(36,150,160,.75),rgba(36,150,160,0)),
    radial-gradient(ellipse 40px 18px at 320px 240px,rgba(60,160,170,.6),rgba(60,160,170,0)),
    radial-gradient(ellipse 200px 160px at 620px 200px,rgba(228,232,238,.95),rgba(228,232,238,0)),
    linear-gradient(100deg,#c7a99a 0%,#d2b8aa 30%,#b9bec8 55%,#c9d0da 80%,#b2bcc9 100%)}
.hero-text{left:0;width:752px;text-align:center;color:var(--white);font-weight:400;text-shadow:0 1px 3px rgba(0,0,0,.18)}
.hero h1{font-size:17px;top:140px;top:8px}
.hero .cta{left:313px;top:253px;width:126px;height:19px;border:1px solid var(--white);border-radius:5px;font-size:8px;line-height:17px;text-align:center;color:var(--white)}
.hero .arrow{top:258px;width:18px;height:18px;border:1px solid rgba(255,255,255,.9);color:var(--white)}
.dots{left:358px;top:383px;display:flex;gap:5px}
.dots i{width:9px;height:9px;border:1px solid var(--white);border-radius:50%}
.dots i.on{background:radial-gradient(var(--white) 30%,transparent 38%)}

/* quick bar */
.quickbar{left:0;top:400px;width:752px;height:35px;border-bottom:1px solid var(--line);background:var(--white)}
.quickbar .ask{left:101px;top:13px;font-size:7px;color:var(--ink);display:flex;align-items:center;gap:4px}
.quickbar .ask i{width:6px;height:6px;border-radius:50%;background:var(--blue)}
.quickbar .field{left:269px;top:10px;width:131px;height:16px;border:1px solid #d5dbe1;border-radius:3px;font-size:5.5px;color:#b3bcc5;padding:4px 0 0 17px;font-style:italic}
.qbtn{top:6px;width:54px;height:24px;background:var(--blue);border-radius:3px;color:var(--white);font-size:6px;font-weight:600;text-align:center;line-height:7px;padding-top:5px}
.qbtn.soft{color:#b8d6fb;font-weight:400}

/* media */
.video{left:101px;top:472px;width:268px;height:118px;
  background:
    radial-gradient(ellipse 30px 50px at 210px 65px,rgba(40,90,160,.8),rgba(40,90,160,0)),
    radial-gradient(ellipse 26px 44px at 120px 60px,rgba(70,120,190,.75),rgba(70,120,190,0)),
    radial-gradient(ellipse 70px 25px at 150px 95px,rgba(240,242,248,.9),rgba(240,242,248,0)),
    radial-gradient(ellipse 50px 70px at 150px 30px,rgba(250,250,255,.9),rgba(250,250,255,0)),
    linear-gradient(90deg,#aeb4d2 0%,#d8dcec 25%,#eef0f7 50%,#c8cfe3 75%,#9ea9c8 100%)}
.play{left:220px;top:517px;width:29px;height:29px;border:2px solid rgba(255,255,255,.9);border-radius:50%}
.play::after{content:"";position:absolute;left:10px;top:7px;border-left:9px solid rgba(255,255,255,.9);border-top:5.5px solid transparent;border-bottom:5.5px solid transparent}
.thumb{top:602px;width:47px;height:47px}
.round{width:15px;height:15px;border:1px solid #d5dbe1;color:#c3cad2}

/* panels */
.panel-head{height:23px;font-size:8.5px;font-weight:600;color:var(--white);padding:6px 10px}
.visit{left:383px;top:472px;width:127px;height:177px;background:var(--blue)}
.visit li{height:19.2px;border-top:1px solid rgba(0,0,0,.13);font-size:6.6px;color:var(--white);padding:5px 10px;position:relative}
.visit li.soft{color:#a5cdfb}
.item-chev{position:absolute;right:8px;top:50%;margin-top:-4px;width:8px;height:8px;border:1px solid currentColor;color:var(--white)}
.portal{left:524px;top:472px;width:127px;height:46px;background:var(--coral)}
.portal .row{display:flex;justify-content:space-around;align-items:center;height:23px;border-top:1px solid rgba(0,0,0,.1);font-size:6.8px;color:var(--white)}
.portal .or{width:11px;height:11px;border-radius:50%;background:var(--coral-dark);font-size:5.5px;text-align:center;line-height:11px}
.res{left:524px;top:530px;width:127px;height:119px;background:var(--coral)}
.res li{height:32px;border-top:1px solid rgba(0,0,0,.1);font-size:6.6px;color:var(--white);padding:5px 24px 0 10px;line-height:11px;position:relative}
.res li.soft{color:#f4b5ad}
.res li.soft .item-chev{color:#f4b5ad}

/* bands */
.band{left:0;width:752px}
.news{top:696px;height:179px;background:var(--slate)}
.col-title{left:101px;font-size:8.5px;font-weight:600}
.col-rule{left:101px;width:33px;height:2px;background:var(--blue)}
.col-copy{left:101px;width:128px;font-size:6.8px;line-height:11.2px}
.more{left:101px;font-size:7px;display:flex;align-items:center;gap:7px}
.more .chev{width:11px;height:11px;background:var(--blue);color:var(--white)}
.card{width:127px;text-align:center}
.card .img{height:77px;position:relative}
.card .date{position:absolute;left:0;top:0;width:22px;height:19px;background:var(--blue);color:var(--white);font-size:6px;font-weight:600;line-height:7px;padding-top:2px}
.card h3{font-size:8.2px;font-weight:600;margin-top:11px}
.card p{font-size:7px;line-height:11.2px;margin-top:4px}

/* footer */
.footer{top:1100px;height:100px;background:var(--slate-dark)}
.flinks{left:101px;top:1129px;display:flex;font-size:7px;font-weight:400;color:var(--white)}
.flinks span{padding:0 9px;border-left:1px solid rgba(255,255,255,.15)}
.flinks span:first-child{padding-left:0;border:0}
.award{left:525px;top:1124px;width:125px;height:20px;background:#2a3a4b;clip-path:polygon(6% 0,94% 0,100% 50%,94% 100%,6% 100%,0 50%)}
.fsocial{left:548px;top:1159px;display:flex;gap:15px}
.fsocial i{width:9px;height:9px;border-radius:2px;background:#4a5d72}
.copy{left:101px;top:1184px;font-size:6px;color:#4e6176}
</style>
</head>
<body>

<div class="abs topbar">
  <span class="item" style="left:101px">About Us</span>
  <i class="sep" style="left:140px"></i>
  <span class="item" style="left:149px">News</span>
  <i class="sep" style="left:177px"></i>
  <span class="item" style="left:186px">Giving</span>
  <span class="item" style="left:313px"><svg width="6" height="6" viewBox="0 0 10 10"><path d="M2 1l2 2-1 1.5c.6 1.2 1.4 2 2.5 2.5L7 6l2 2-1.5 1.5C4.5 9 1 5.5.5 2.5z" fill="#8fa2b6"/></svg>(555) 014 - 2200</span>
  <span class="item" style="left:392px"><svg width="7" height="5" viewBox="0 0 14 10"><rect x=".5" y=".5" width="13" height="9" fill="none" stroke="#8fa2b6"/><path d="M.5.5L7 6 13.5.5" fill="none" stroke="#8fa2b6"/></svg>Contact Us</span>
  <span class="item" style="left:555px;color:#7d90a4">&#9113;</span>
  <span class="item" style="left:582px;color:#7d90a4">A</span>
  <span class="item" style="left:608px"><i style="width:6px;height:6px;border-radius:50%;background:#7d90a4"></i>English <span style="color:#7d90a4">&#9662;</span></span>
</div>

<header class="abs header">
  <div class="abs social"><i></i><i></i><i></i><i></i></div>
  <div class="abs logo"><span class="mark"></span><span class="name">BRACKFIELD HOSPITAL</span></div>
  <div class="abs search">Search...<b><svg width="7" height="7" viewBox="0 0 10 10"><circle cx="4" cy="4" r="3" fill="none" stroke="#fff" stroke-width="1.4"/><path d="M6.2 6.2L9 9" stroke="#fff" stroke-width="1.4"/></svg></b></div>
</header>

<nav class="abs nav">
  <a class="active" style="left:101px;width:89px">Our Services</a>
  <a style="left:190px;width:119px">Facilities &amp; Directions</a>
  <a style="left:309px;width:143px">Patient &amp; Visitor Information</a>
  <a style="left:452px;width:91px">Find a Doctor</a>
  <a style="left:543px;width:108px;border-right:1px solid rgba(0,0,0,.14)">Health &amp; Wellness</a>
</nav>

<section class="abs hero" role="img" aria-label="Smiling young girl in a hospital bed with a nurse holding a stethoscope"></section>
<h1 class="abs hero-text" style="top:219px;font-size:17px">We Will Make a Healthy Difference in the Lives We Touch</h1>
<h2 class="abs hero-text" style="top:250px;font-size:16px;line-height:19px">The best doctors and nurses, and<br>treatment close to home.</h2>
<a class="abs cta hero-cta" style="left:313px;top:308px;width:126px;height:19px;border:1px solid #fff;border-radius:5px;font-size:8px;line-height:17px;text-align:center;color:#fff">Find out more about us</a>
<i class="abs chev left" style="left:28px;top:257px;width:18px;height:18px;border:1px solid rgba(255,255,255,.9);color:#fff"></i>
<i class="abs chev" style="left:707px;top:257px;width:18px;height:18px;border:1px solid rgba(255,255,255,.9);color:#fff"></i>
<div class="abs dots" style="top:383px"><i class="on"></i><i></i><i></i></div>

<div class="abs quickbar">
  <div class="abs ask"><i></i>Do you want to learn about a condition?</div>
  <div class="abs field">Diabetes, Cancer, Heart Health...</div>
  <a class="abs qbtn" style="left:414px">Symptom<br>Checker</a>
  <a class="abs qbtn soft" style="left:475px">Schedule a<br>Lab Test</a>
  <a class="abs qbtn" style="left:535px">Online Bill<br>Pay</a>
  <a class="abs qbtn" style="left:597px">Support Our<br>Work</a>
</div>

<div class="abs video" role="img" aria-label="Video still of medical staff wheeling a patient bed down a hospital corridor"></div>
<i class="abs play"></i>
<i class="abs chev left round" style="left:101px;top:618px"></i>
<div class="abs thumb" role="img" aria-label="Hand using a touch screen" style="left:129px;background:radial-gradient(circle at 60% 45%,#e8eef6,#9db6d3 55%,#6f8fb6)"></div>
<div class="abs thumb" role="img" aria-label="Staff in a bright hospital hallway" style="left:184px;background:radial-gradient(ellipse at 50% 35%,#f1f6fb,#8fb6d8 50%,#3f78b0)"></div>
<div class="abs thumb" role="img" aria-label="Patient monitor screen" style="left:239px;background:radial-gradient(ellipse at 55% 40%,#6a7fa0,#3a3f52 55%,#b29ea0)"></div>
<div class="abs thumb" role="img" aria-label="Medical equipment close-up" style="left:294px;background:linear-gradient(135deg,#2b2e38,#5d6274 45%,#d8dbe2 60%,#3a3e4a)"></div>
<i class="abs chev round" style="left:354px;top:618px;background:#d5dbe1;color:#fff;border-color:#d5dbe1"></i>

<div class="abs visit">
  <div class="panel-head">About Your Visit</div>
  <ul>
    <li>Emergency Care<i class="chev item-chev"></i></li>
    <li>Accepted Health Plans<i class="chev item-chev"></i></li>
    <li class="soft">Pre-registration for Surgery<i class="chev item-chev" style="color:#a5cdfb"></i></li>
    <li>Lab Hours<i class="chev item-chev"></i></li>
    <li>Schedule a Lab Test<i class="chev item-chev"></i></li>
    <li>Find a Phone Number<i class="chev item-chev"></i></li>
    <li>Find a Form<i class="chev item-chev"></i></li>
    <li>Visitor Guide<i class="chev item-chev"></i></li>
  </ul>
</div>

<div class="abs portal">
  <div class="panel-head">Brackfield Patient Portal</div>
  <div class="row"><span>Login</span><span class="or">or</span><span style="color:#f4b5ad">Register</span></div>
</div>

<div class="abs res">
  <div class="panel-head">Patient Resources</div>
  <ul>
    <li>Tips to Choose the Right Doctor<i class="chev item-chev"></i></li>
    <li class="soft">Billing, Forms, &amp; Medical Records<i class="chev item-chev"></i></li>
    <li>Making the Most of Your Appointment<i class="chev item-chev"></i></li>
  </ul>
</div>

<section class="abs band news">
  <h2 class="abs col-title" style="top:28px;color:var(--white)">BH News</h2>
  <i class="abs col-rule" style="top:47px"></i>
  <p class="abs col-copy" style="top:57px;color:#9aa9b8">Lorem ipsum dolor sit amet, consectetur adipiscing elit. Mauris bibendum diam sapien, nec tristique tellus condimentum quis. Curabitur ut ipsum neque. Donec ultricies sollicitudin eros.</p>
  <a class="abs more" style="top:144px;color:var(--white)">View More <i class="chev"></i></a>
  <article class="abs card" style="left:242px;top:29px">
    <div class="img" role="img" aria-label="Doctor in white coat with stethoscope" style="background:radial-gradient(ellipse 20px 26px at 30% 35%,rgba(60,60,70,.55),rgba(60,60,70,0)),radial-gradient(ellipse 60px 40px at 60% 80%,#c9ccd3,rgba(201,204,211,0)),linear-gradient(90deg,#f4f4f6,#e2e4e9 50%,#f6f6f8)"><span class="date">29<br>SEP</span></div>
    <h3 style="color:var(--white)">Lorem ipsum dolor sit amet</h3>
    <p style="color:#b5c1cd">Donec eget feugiat leo. Phasellus commodo tincidunt ornare.</p>
  </article>
  <article class="abs card" style="left:383px;top:29px">
    <div class="img" role="img" aria-label="Nurse talking with an elderly patient" style="background:radial-gradient(ellipse 30px 35px at 75% 55%,rgba(40,55,90,.85),rgba(40,55,90,0)),radial-gradient(ellipse 35px 30px at 28% 55%,rgba(225,205,190,.9),rgba(225,205,190,0)),linear-gradient(90deg,#c3c9d4,#8e98aa 55%,#6e7a8e)"><span class="date">29<br>SEP</span></div>
    <h3 style="color:#b5c1cd">Lorem ipsum dolor sit amet</h3>
    <p style="color:#b5c1cd">Donec eget feugiat leo. Phasellus commodo tincidunt ornare.</p>
  </article>
  <article class="abs card" style="left:524px;top:29px">
    <div class="img" role="img" aria-label="Staff moving a hospital bed in a corridor" style="background:radial-gradient(ellipse 14px 28px at 75% 45%,rgba(50,100,170,.8),rgba(50,100,170,0)),radial-gradient(ellipse 12px 22px at 45% 45%,rgba(70,120,180,.7),rgba(70,120,180,0)),radial-gradient(ellipse 40px 15px at 50% 80%,#f4f5f8,rgba(244,245,248,0)),linear-gradient(90deg,#c7b8b4,#e6e8ee 40%,#dfe3ea 70%,#b7c0cc)"><span class="date">29<br>SEP</span></div>
    <h3 style="color:#b5c1cd">Lorem ipsum dolor sit amet</h3>
    <p style="color:#b5c1cd">Donec eget feugiat leo. Phasellus commodo tincidunt ornare.</p>
  </article>
</section>

<section class="abs band" style="top:875px;height:225px">
  <h2 class="abs col-title" style="top:45px;color:var(--ink);font-weight:400">Upcoming Classes &amp; Events</h2>
  <p class="abs col-copy" style="top:80px;color:#a7b1bb">Lorem ipsum dolor sit amet, consectetur adipiscing elit. Mauris bibendum diam sapien, nec tristique tellus condimentum quis. Curabitur ut ipsum neque. Donec ultricies sollicitudin eros.</p>
  <a class="abs more" style="top:167px;color:var(--ink)">View More <i class="chev"></i></a>
  <article class="abs card" style="left:242px;top:47px">
    <div class="img" role="img" aria-label="Pregnant woman in a red dress" style="background:radial-gradient(ellipse 40px 30px at 55% 75%,rgba(170,40,50,.85),rgba(170,40,50,0)),radial-gradient(ellipse 30px 25px at 40% 25%,rgba(110,50,40,.8),rgba(110,50,40,0)),linear-gradient(90deg,#d98a78,#b4564e 50%,#e6a48d)"><span class="date">29<br>SEP</span></div>
    <h3 style="color:var(--blue)">Lorem ipsum dolor sit amet</h3>
    <p style="color:#a7b1bb">Donec eget feugiat leo. Phasellus commodo tincidunt ornare.</p>
  </article>
  <article class="abs card" style="left:383px;top:47px">
    <div class="img" role="img" aria-label="Doctor holding a heart model with digital charts" style="background:radial-gradient(circle 7px at 52% 55%,rgba(215,40,50,.9),rgba(215,40,50,0)),radial-gradient(ellipse 24px 40px at 48% 60%,rgba(250,252,255,.95),rgba(250,252,255,0)),linear-gradient(135deg,#b9c9dd,#e4ebf4 50%,#a9bcd4)"><span class="date">29<br>SEP</span></div>
    <h3 style="color:#8c97a3;font-weight:400">Lorem ipsum dolor sit amet</h3>
    <p style="color:#a7b1bb">Donec eget feugiat leo. Phasellus commodo tincidunt ornare.</p>
  </article>
  <article class="abs card" style="left:524px;top:47px">
    <div class="img" role="img" aria-label="Surgeons working in an operating room" style="background:radial-gradient(ellipse 22px 36px at 25% 65%,rgba(30,50,90,.85),rgba(30,50,90,0)),radial-gradient(ellipse 22px 36px at 75% 65%,rgba(40,70,120,.85),rgba(40,70,120,0)),radial-gradient(ellipse 30px 14px at 45% 15%,#eef1f5,rgba(238,241,245,0)),linear-gradient(180deg,#aab7c6,#7d93ad 60%,#5f7796)"><span class="date">29<br>SEP</span></div>
    <h3 style="color:#8c97a3;font-weight:400">Lorem ipsum dolor sit amet</h3>
    <p style="color:#a7b1bb">Donec eget feugiat leo. Phasellus commodo tincidunt ornare.</p>
  </article>
</section>

<footer class="abs band footer"></footer>
<div class="abs flinks">
  <span>Referring Physicians</span><span>Medical Professionals</span><span>Giving</span><span>Volunteering</span><span>Careers</span><span>Online Bill Pay</span>
</div>
<div class="abs award" role="img" aria-label="Awards badge"></div>
<div class="abs fsocial"><i></i><i></i><i></i><i></i></div>
<p class="abs copy">Copyright &copy; 2014 Brackfield Hospital - All Rights Reserved.</p>

</body>
</html>
```